Stationary for New Company

We need stationary designed for a new company. Details of the required stationary is attached.

The final version should be trendy, clean... only 2 colours (green + grey/black) and professional.

#1: Business Cards (design on 2 sides)
#2: Letterhead (word format)
#3: Cover Page and back cover for proposals
#4: Envelopes,
#5: Thank You card,
#6: Presentation Folder,
#7: Email signatures template (sample attached in word document)

Logo is attached. Logo can be reversed out (will attach once available). Logo can be stacked or horizontal (provided as horizontal).

Files need to be provided in ai + png format.

Target Market(s)

Business owners. More affluent.

Industry/Entity Type

Business

Requirements
Must have
• See brief

Font: Calibri
Should not have
• Photographs / stock photos

```html
<!DOCTYPE html>
<html lang="en">
<head>
<meta charset="utf-8">
<title>Northgate Insurance Brokers – Stationery Suite</title>
<link rel="stylesheet" href="https://fonts.googleapis.com/css2?family=Carlito:wght@400;700&display=swap">
<style>
:root{
  --green:#6b9138;
  --green-light:#9fc95f;
  --grey:#7b7b7b;
  --grey-light:#b9b9b9;
  --ink:#333;
  --paper:#fff;
  --board:#4b4b4b;
  --die:#d33;
}
*{box-sizing:border-box;margin:0;padding:0}
html,body{width:1200px;height:800px;overflow:hidden;background:var(--board);font-family:"Carlito",sans-serif;color:var(--ink)}
.board{position:relative;width:1200px;height:800px}
.piece{position:absolute;background:var(--paper);overflow:hidden}
.bar{position:absolute;left:0;right:0}
.bar--grey{background:var(--grey)}
.bar--green{background:var(--green)}
.brand{display:flex;align-items:center;gap:5px;color:var(--green);white-space:nowrap;line-height:1}
.brand__mark{background:var(--green);flex:none}
.brand__name{font-weight:400}
.abs{position:absolute}
.tiny{font-size:4px;line-height:1.35;color:var(--ink)}
.label{color:var(--green)}

/* letterhead */
.letterhead{left:22px;top:35px;width:322px;height:415px}
.letterhead .brand{position:absolute;left:88px;top:20px}
.letterhead .brand__mark{width:30px;height:30px}
.letterhead .brand__name{font-size:19px}
.letterhead .brand__sub{font-size:10px;color:var(--grey)}
.letterhead__title{position:absolute;left:66px;top:83px;font-size:10px;font-weight:700;color:var(--green)}
.letterhead__body{position:absolute;left:66px;top:104px;width:240px;font-size:4.8px;line-height:1.55;color:#555}
.letterhead__body p{margin-bottom:6px}
.signature{position:absolute;left:185px;top:305px;width:48px;height:26px;background:linear-gradient(90deg,#e9e4f2,#d8cfe8);border-radius:3px}
.seal{position:absolute;left:236px;top:300px;width:40px;height:40px;border-radius:50%;border:2px solid #8a7fb8}
.letterhead__foot{position:absolute;left:0;right:0;top:370px;text-align:center;font-size:6.2px;line-height:1.5}

/* envelope */
.envelope{left:364px;top:22px;width:325px;height:138px}
.envelope .brand{position:absolute;left:5px;top:9px}
.envelope .brand__mark{width:15px;height:15px}
.envelope .brand__name{font-size:11px}

/* business card */
.card{left:765px;top:22px;width:415px;height:188px}
.card .brand{position:absolute;left:97px;top:24px}
.card .brand__mark{width:30px;height:30px}
.card .brand__name{font-size:21px}
.card__person{position:absolute;left:0;right:0;top:78px;text-align:center;font-size:10px}
.card__person strong{display:block;color:var(--green);font-size:10.5px}
.card__web{position:absolute;left:0;right:0;top:113px;text-align:center;font-size:9px;color:var(--grey);line-height:1.25}
.card__grid{position:absolute;top:152px;font-size:8.5px;line-height:1.4}

/* folder */
.folder{left:366px;top:180px;width:384px;height:318px;background:var(--paper)}
.folder svg{position:absolute;left:0;top:0}
.folder__cover{position:absolute;left:192px;top:10px;width:192px;height:222px}
.folder__cover .brand{position:absolute;left:18px;top:96px}
.folder__cover .brand__mark{width:34px;height:34px}
.folder__cover .brand__name{font-size:19px}
.folder__back-text{position:absolute;left:62px;top:202px;color:#fff;font-size:3.6px;line-height:1.4;text-align:center;width:110px}

/* thank you */
.thanks{left:910px;top:248px;width:270px;height:196px}
.thanks svg{position:absolute;left:0;top:0}
.thanks__lead{position:absolute;left:24px;top:19px;font-size:11px;color:var(--grey)}
.thanks__big{position:absolute;left:48px;top:38px;font-size:30px;line-height:.9;color:#fff}
.thanks__big span{display:block;padding-left:46px}
.thanks__tail{position:absolute;left:164px;top:90px;font-size:10px;color:var(--grey)}
.thanks .brand{position:absolute;left:48px;top:124px}
.thanks .brand__mark{width:34px;height:34px}
.thanks .brand__name{font-size:17px}

/* small envelope */
.envelope-small{left:910px;top:455px;width:270px;height:184px}
.envelope-small .brand{position:absolute;left:8px;top:13px}
.envelope-small .brand__mark{width:24px;height:24px}
.envelope-small .brand__name{font-size:13px}

/* covers */
.cover{top:508px;width:215px;height:283px}
.cover--front{left:22px}
.cover--back{left:250px}
.cover__band{position:absolute;top:0;bottom:0;background:var(--green-light)}
.cover--front .cover__band{left:146px;width:69px}
.cover--back .cover__band{left:150px;width:65px}
.cover__client{position:absolute;left:24px;top:32px;font-size:7px;font-weight:700;color:var(--grey)}
.cover__year{position:absolute;left:150px;top:44px;font-size:11px;font-weight:700;color:#fff}
.cover__tag{position:absolute;left:38px;top:79px;width:138px;height:11px;background:var(--grey);color:#fff;font-size:6.5px;font-weight:700;padding-left:20px;line-height:11px}
.cover--front .brand{position:absolute;left:80px;top:117px}
.cover--front .brand__mark{width:26px;height:26px}
.cover--front .brand__name{font-size:16px}
.cover__person{position:absolute;left:44px;top:218px;font-size:8px;text-align:center;width:80px}
.cover__person strong{display:block;color:var(--green);font-size:7px}
.cover--back .brand{position:absolute;left:15px;top:22px}
.cover--back .brand__mark{width:14px;height:14px}
.cover--back .brand__name{font-size:9px}

/* letter sheets */
.sheet{width:224px}
.sheet--rear{left:675px;top:435px;height:285px}
.sheet--front{left:487px;top:503px;height:290px}
.sheet .brand__mark{width:16px;height:16px}
.sheet .brand__name{font-size:12px}
</style>
</head>
<body>
<main class="board">

  <section class="piece letterhead" aria-label="Letterhead">
    <div class="bar bar--grey" style="top:5px;height:7px"></div>
    <div class="brand">
      <span class="brand__mark"></span>
      <span><span class="brand__name">Northgate</span><br><span class="brand__sub">Insurance Brokers</span></span>
    </div>
    <h1 class="letterhead__title">SAMPLE TEXT HERE</h1>
    <div class="letterhead__body">
      <p>Lorem ipsum dolor sit amet, consectetur adipiscing elit. Pellentesque tristique elementum sem. Quisque eget erat ac lectus sodales faucibus. Nam commodo est. Cras consequat faucibus velit. Nam ac magna. Sed et ligula. Nam volutpat, elit ac facilisis tempor, neque euismod leo, sit amet molestie sem est eu libero. Nulla facilisi. Pellentesque sit amet odio.</p>
      <p>In dui turpis, varius vitae, tincidunt id, consequat ut, leo. Donec tincidunt tristique odio. Nulla erat felis, euismod nec, fringilla non, aliquet et, magna. Nulla at magna quis nisl pretium vehicula. Pellentesque habitant morbi tristique senectus et netus et malesuada fames ac turpis egestas. Class aptent taciti sociosqu ad litora torquent per conubia nostra.</p>
      <p>Nunc purus. Cras auctor, in ornare neque ligula. Nulla tincidunt, diam sit amet viverra euismod, sapien augue fringilla neque, at pellentesque felis tortor vel enim. Etiam dignissim. Sed a tortor vel nisl euismod ultricies. Donec molestie congue luctus. Integer sed turpis a tortor imperdiet consequat. Maecenas molestie placerat urna.</p>
      <p>Nulla lobortis ultricies nulla. Pellentesque purus mi, consequat quis, hendrerit sed, imperdiet non, eros. Nullam urna est, vehicula nec, cursus nec, dignissim sit amet, risus. Duis molestie, tellus sit amet laoreet ullamcorper, urna orci fringilla ante, at rhoncus justo dolor vel dui. Praesent sed justo sed arcu commodo feugiat.</p>
    </div>
    <div class="signature" role="img" aria-label="Handwritten signature"></div>
    <div class="seal" role="img" aria-label="Company seal"></div>
    <div class="letterhead__foot">
      4820 Cedar Lane NW Westbrook, AB T5X 2L9<br>
      <span class="label">Phone:</span> 555.210.4400 <span class="label">Fax:</span> 555.210.4401 <span class="label">Toll Free:</span> 888.555.0192<br>
      <span class="label">Website:</span> www.northgateinsure.com
    </div>
    <div class="bar bar--green" style="top:399px;height:4px"></div>
    <div class="bar bar--grey" style="top:404px;height:6px"></div>
  </section>

  <section class="piece envelope" aria-label="Envelope">
    <div class="brand"><span class="brand__mark"></span><span class="brand__name">Northgate</span></div>
    <div class="abs tiny" style="left:134px;top:106px">Website: www.northgateinsure.com<br>4820 Cedar Lane NW Westbrook, AB T5X 2L9<br><span class="label">Phone:</span> 555.210.4400 <span class="label">Fax:</span> 555.210.4401 <span class="label">Toll Free:</span> 888.555.0192</div>
    <div class="bar bar--green" style="top:127px;height:3px"></div>
    <div class="bar bar--grey" style="top:130px;height:8px"></div>
  </section>

  <section class="piece card" aria-label="Business card">
    <div class="bar bar--green" style="top:0;height:4px"></div>
    <div class="bar bar--grey" style="top:4px;height:3px"></div>
    <div class="brand">
      <span class="brand__mark"></span>
      <span><span class="brand__name">Northgate</span><br><span style="font-size:10px;color:var(--grey)">Insurance Brokers</span></span>
    </div>
    <div class="card__person">Daniel Reyes, BA, CRM<strong>President &amp; CEO</strong></div>
    <div class="card__web">www.northgateinsure.com<br>Email: dreyes@northgateinsure.com</div>
    <div class="card__grid" style="left:23px">4820 Cedar Lane NW<br>Westbrook, AB T5X 2L9</div>
    <div class="card__grid" style="left:134px"><span class="label">Phone:</span> 555.210.4400<br><span class="label">Direct:</span> 555.210.4499</div>
    <div class="card__grid" style="left:255px"><span class="label">Fax:</span> 555.210.4401<br><span class="label">Toll Free:</span> 888.555.0192</div>
    <div class="bar bar--green" style="top:178px;height:10px"></div>
  </section>

  <section class="piece folder" aria-label="Presentation folder">
    <svg width="384" height="318" viewBox="0 0 384 318" aria-hidden="true">
      <rect x="8" y="10" width="184" height="222" fill="var(--green)"/>
      <rect x="8" y="6" width="376" height="4" fill="var(--grey)"/>
      <rect x="192" y="10" width="192" height="222" fill="#fff" stroke="#ddd" stroke-width=".5"/>
      <rect x="8" y="227" width="376" height="5" fill="var(--grey)"/>
      <polyline points="8,150 8,165 0,165 6,230 8,232" fill="none" stroke="var(--die)" stroke-width=".8"/>
      <polyline points="8,232 22,306 185,306 190,236" fill="#fff" stroke="var(--die)" stroke-width=".8"/>
      <polygon points="194,236 384,236 384,306 210,306" fill="var(--green)" stroke="var(--die)" stroke-width=".8"/>
      <rect x="70" y="255" width="70" height="4" fill="var(--grey)"/>
      <line x1="74" y1="252" x2="144" y2="252" stroke="#3a8bd1" stroke-width=".8"/>
      <line x1="70" y1="285" x2="142" y2="285" stroke="#3a8bd1" stroke-width=".8"/>
      <rect x="110" y="280" width="5" height="5" fill="var(--green)"/>
    </svg>
    <div class="folder__cover">
      <div class="brand">
        <span class="brand__mark"></span>
        <span><span class="brand__name">Northgate</span><br><span style="font-size:10px;color:var(--grey)">Insurance Brokers</span></span>
      </div>
    </div>
    <div class="folder__back-text">4820 Cedar Lane NW Westbrook, AB T5X 2L9<br>Phone: 555.210.4400 Fax: 555.210.4401 Toll Free: 888.555.0192<br>Website: www.northgateinsure.com</div>
  </section>

  <section class="piece thanks" aria-label="Thank you card">
    <svg width="270" height="196" viewBox="0 0 270 196" aria-hidden="true">
      <polygon points="110,0 270,0 270,12 170,19" fill="var(--grey)"/>
      <polygon points="0,36 270,12 270,78 0,88" fill="var(--green)"/>
      <polygon points="0,88 150,83 0,100" fill="var(--grey-light)"/>
      <rect x="0" y="189" width="270" height="7" fill="var(--grey)"/>
    </svg>
    <div class="thanks__lead">We would like to say</div>
    <div class="thanks__big">Thank<span>You</span></div>
    <div class="thanks__tail">for your business</div>
    <div class="brand">
      <span class="brand__mark"></span>
      <span><span class="brand__name">Northgate</span><br><span style="font-size:10px;color:var(--grey)">Insurance Brokers</span></span>
    </div>
  </section>

  <section class="piece envelope-small" aria-label="Envelope">
    <div class="brand"><span class="brand__mark"></span><span><span class="brand__name">Northgate</span><br><span style="font-size:7px;color:var(--grey)">Insurance Brokers</span></span></div>
    <div class="abs tiny" style="left:84px;top:154px;text-align:right;width:110px">Website: www.northgateinsure.com<br>4820 Cedar Lane NW Westbrook, AB T5X 2L9<br><span class="label">Phone:</span> 555.210.4400 <span class="label">Fax:</span> 555.210.4401</div>
    <div class="bar bar--green" style="top:172px;height:3px"></div>
    <div class="bar bar--grey" style="top:175px;height:9px"></div>
  </section>

  <section class="piece cover cover--front" aria-label="Proposal front cover">
    <div class="cover__band"></div>
    <div class="cover__client">Corvane Medical Inc.</div>
    <div class="cover__year">2014 - 2015</div>
    <div class="cover__tag">Insurance Program Portfolio</div>
    <div class="brand">
      <span class="brand__mark"></span>
      <span><span class="brand__name">Northgate</span><br><span style="font-size:8px;color:var(--grey)">Insurance Brokers</span></span>
    </div>
    <div class="abs tiny" style="left:150px;top:170px;color:#fff">Daniel Reyes, BA, CRM<br>Partner, Westbrook Office<br>Direct: 555.210.4499<br>Email: dreyes@northgate.ca<br><br>Alana Brooks, CIB<br>Account Executive<br>Direct: 555.210.4460<br>Email: abrooks@northgate.ca<br><br>Mara Quinn, CIB<br>Client Service Lead<br>Direct: 555.210.4470<br>Email: mquinn@northgate.ca</div>
    <div class="cover__person">Daniel Reyes, BA, CRM<strong>President &amp; CEO</strong></div>
    <div class="abs tiny" style="left:20px;top:256px;text-align:center;width:130px">www.northgateinsure.com<br>4820 Cedar Lane NW Westbrook, AB T5X 2L9<br><span class="label">Phone:</span> 555.210.4400 <span class="label">Fax:</span> 555.210.4401 <span class="label">Toll Free:</span> 888.555.0192</div>
  </section>

  <section class="piece cover cover--back" aria-label="Proposal back cover">
    <div class="cover__band"></div>
    <div class="brand"><span class="brand__mark"></span><span class="brand__name">Northgate</span></div>
    <div class="abs tiny" style="left:154px;top:212px;color:#fff">4820 Cedar Lane NW<br>Westbrook, AB T5X 2L9<br><br>Phone: 555.210.4400<br>Fax: 555.210.4401<br>Toll Free: 888.555.0192<br><br>www.northgateinsure.com</div>
  </section>

  <section class="piece sheet sheet--front" aria-label="Letter template">
    <div class="bar bar--grey" style="top:0;height:7px"></div>
    <div class="abs tiny" style="left:10px;top:242px">Daniel Reyes, BA, CRM<br>Partner, Westbrook Head Office<br><span style="color:#999">4820 Cedar Lane<br>Suite 210<br>Westbrook, Alberta<br>T5X 2L9</span></div>
    <div class="brand abs" style="left:115px;top:246px"><span class="brand__mark"></span><span class="brand__name">Northgate</span></div>
    <div class="abs tiny" style="left:10px;top:271px">Direct: +1.555.210.4499 | Mobile: +1.555.210.4488 | Fax: +1.555.210.4401 | Email: dreyes@northgate.ca</div>
    <div class="bar bar--green" style="top:279px;height:3px"></div>
    <div class="bar bar--grey" style="top:282px;height:8px"></div>
  </section>

  <section class="piece sheet sheet--rear" aria-label="Letter template">
    <div class="bar bar--grey" style="top:0;height:7px"></div>
    <div class="abs tiny" style="left:8px;top:227px">Daniel Reyes, BA, CRM<br>Partner, Westbrook Head Office<br><br>Direct: +1.555.210.4499 | Mobile: +1.555.210.4488 | Fax: +1.555.210.4401 | Email: dreyes@northgate.ca</div>
    <div class="brand abs" style="left:10px;top:252px"><span class="brand__mark"></span><span class="brand__name">Northgate</span></div>
    <div class="abs tiny" style="left:105px;top:252px;color:#999">4820 Cedar Lane<br>Suite 210<br>Westbrook, Alberta<br>T5X 2L9</div>
    <div class="bar bar--green" style="top:275px;height:3px"></div>
    <div class="bar bar--grey" style="top:278px;height:7px"></div>
  </section>

</main>
</body>
</html>
```